Menu Design Project

We are a post colonial tavern serving craft beer, local wine and fine spirits. Our colors are black, copper and old brick. We are on a town square,...

Town

```html
<!DOCTYPE html>
<html lang="en">
<head>
<meta charset="utf-8">
<title>Hollis Tavern Menu</title>
<link href="https://fonts.googleapis.com/css2?family=Cormorant+Garamond:wght@600;700&family=Noto+Serif:ital,wght@0,400;1,400&display=swap" rel="stylesheet">
<style>
:root{
  --page:#ffffff;
  --panel:#2b2927;
  --panel-deep:#1f1d1c;
  --copper:#b38c5e;
  --copper-soft:#9c7a54;
  --ink:#e4ddd2;
  --ink-dim:#bdb5a9;
  --brick-hi:#8a4326;
  --brick-mid:#5e2e1c;
  --brick-low:#241915;
  --rule:#7c6a55;
}
*{box-sizing:border-box;margin:0;padding:0}
html,body{width:1200px;height:1000px;overflow:hidden;background:var(--page)}
body{position:relative;font-family:"Noto Serif",Georgia,serif;color:var(--ink)}
.brick{position:absolute;background:radial-gradient(ellipse at 50% 45%,var(--brick-hi) 0%,var(--brick-mid) 55%,var(--brick-low) 100%)}
.wordmark{position:absolute;font-family:"Cormorant Garamond",Georgia,serif;font-weight:700;color:#f4efe8;white-space:nowrap;line-height:1}

/* cover */
.cover{position:absolute;left:117px;top:137px;width:304px;height:466px;overflow:hidden}
.cover .brick{inset:0}
.cover .fold{position:absolute;left:151px;top:0;width:1px;height:100%;background:rgba(255,255,255,.35)}
.cover .wordmark{left:0;width:100%;top:268px;text-align:center;font-size:34px}

/* inside spread top */
.spread-top{position:absolute;left:460px;top:27px;width:605px;height:466px;overflow:hidden;background:var(--panel-deep)}
.spread-top .brick-left{left:0;top:0;width:148px;height:100%}
.spread-top .brick-right{left:336px;top:0;width:269px;height:100%}
.spread-top .wm-left{left:-70px;top:170px;font-size:36px}
.spread-top .wm-right{left:520px;top:170px;font-size:36px}
.center-col{position:absolute;left:148px;top:0;width:188px;height:100%;background:var(--panel)}
.kids-box{position:absolute;left:16px;top:33px;width:156px;height:277px;border:1.5px solid var(--copper);padding:8px 6px}
.box-title{font-family:"Cormorant Garamond",serif;font-weight:700;color:var(--copper);font-size:12px;letter-spacing:1.5px;text-align:center;margin-bottom:8px}
.sub-title{font-family:"Cormorant Garamond",serif;font-weight:700;color:var(--copper);font-size:9px;letter-spacing:.8px;text-decoration:underline;margin:8px 0 3px}
.side-list{list-style:none;font-size:7.5px;line-height:11px;color:var(--ink)}
.side-list li::before{content:"";display:inline-block;width:5px;height:5px;background:var(--ink);margin-right:4px}
.bev{position:absolute;left:18px;top:344px;width:160px}
.bev-title{font-family:"Cormorant Garamond",serif;font-weight:700;color:var(--copper);font-size:14px;letter-spacing:1px}
.bev-list{font-size:7.5px;line-height:10.5px;color:var(--ink)}
.notice{position:absolute;left:16px;top:431px;width:160px;font-size:5px;line-height:6.5px;color:var(--copper-soft);text-transform:uppercase}

/* items */
.item{margin-bottom:6px}
.item-head{display:flex;align-items:baseline;font-size:8px;color:var(--copper);font-family:"Noto Serif",serif}
.leader{flex:1;border-bottom:1px dotted var(--copper-soft);margin:0 1px;transform:translateY(-2px)}
.price{font-size:5px}
.desc{font-size:4.8px;line-height:6.1px;font-style:italic;color:var(--ink-dim);margin-top:1px}
.addon{font-size:4.8px;line-height:6.1px;color:var(--copper-soft)}
.note{font-size:5px;color:var(--ink-dim);font-style:italic;margin-bottom:5px}

/* bottom spread */
.spread-bottom{position:absolute;left:460px;top:506px;width:605px;height:467px;background:var(--panel);overflow:hidden}
.col{position:absolute;top:0;height:100%;padding:14px 12px 0}
.col-starters{left:0;width:152px}
.col-entrees{left:152px;width:303px;border-left:1px solid var(--rule);border-right:1px solid var(--rule)}
.col-greens{left:455px;width:150px}
.col-title{font-family:"Cormorant Garamond",serif;font-weight:700;color:var(--copper);font-size:14.5px;letter-spacing:.8px;text-align:center;margin-bottom:14px;white-space:nowrap}
.col-starters .item{margin-bottom:8px}
.col-entrees .item{margin-bottom:8.5px}
.section-rule{border-top:1px solid var(--rule);margin:10px -8px 14px}
</style>
</head>
<body>

<section class="cover">
  <div class="brick" style="inset:0" role="img" aria-label="Photograph of an old red brick wall"></div>
  <div class="fold"></div>
  <div class="wordmark">Hollis Tavern</div>
</section>

<section class="spread-top">
  <div class="brick brick-left" role="img" aria-label="Photograph of an old red brick wall"></div>
  <div class="brick brick-right" role="img" aria-label="Photograph of an old red brick wall"></div>
  <div class="wordmark wm-left">Hollis Tavern</div>
  <div class="wordmark wm-right">Hollis Tavern</div>

  <div class="center-col">
    <div class="kids-box">
      <h2 class="box-title">KIDS</h2>
      <div class="item" style="margin-bottom:1px"><div class="item-head">Chicken Tenders<span class="leader"></span><span class="price">6</span></div></div>
      <div class="item" style="margin-bottom:1px"><div class="item-head">Corndog<span class="leader"></span><span class="price">6</span></div></div>
      <div class="item" style="margin-bottom:6px"><div class="item-head">Grilled Cheese<span class="leader"></span><span class="price">6</span></div></div>
      <p class="note">All kids meals served with your choice of side.</p>
      <h3 class="sub-title">SIDES</h3>
      <ul class="side-list">
        <li>Creole Seasoned Fries Rice</li>
        <li>Pilaf Onion Rings</li>
        <li>Sweet Potato Fries</li>
        <li>Grilled Broccoli</li>
      </ul>
      <h3 class="sub-title" style="margin-top:14px">DESSERT</h3>
      <div class="item"><div class="item-head">Southern Deep-Fried Cream Cakes<span class="leader"></span><span class="price">8</span></div>
        <p class="desc">Two cream cakes, deep-fried and glazed with banana icing and a scoop of vanilla bean ice cream.</p></div>
      <div class="item"><div class="item-head">Cookie Ice Cream Sandwich<span class="leader"></span><span class="price">7</span></div>
        <p class="desc">A warm, melted macadamia nut cookie served hot with a scoop of vanilla bean ice cream and sprinkled with coconut, whipped cream and cherry.</p></div>
      <div class="item"><div class="item-head">Chattanooga Deep-Fried Marsh Pie<span class="leader"></span><span class="price">8</span></div>
        <p class="desc">Chocolate or vanilla marsh pie deep-fried and topped with vanilla bean ice cream, whipped cream and a cherry.</p></div>
    </div>

    <div class="bev">
      <h2 class="bev-title">BEVERAGES</h2>
      <p class="bev-list">Classic Cola / Diet Cola / Lemon-Lime Soda / Spiced Cherry Soda / Lemonade / Sweet Tea / Unsweet Tea / Coffee<span style="font-size:5px">..........2</span></p>
    </div>
    <p class="notice">*Consuming raw or undercooked meats, poultry, seafood, shellfish, or eggs may increase your risk of foodborne illness.</p>
  </div>
</section>

<section class="spread-bottom">
  <div class="col col-starters">
    <h2 class="col-title">HORS D’OEUVRES</h2>
    <div class="item"><div class="item-head">Calamari<span class="leader"></span><span class="price">9</span></div><p class="desc">Tender squid lightly floured then deep-fried, served with fresh lemon wedges and marinara sauce.</p></div>
    <div class="item"><div class="item-head">Coconut Shrimp<span class="leader"></span><span class="price">9</span></div><p class="desc">Six jumbo shrimp battered in coconut flakes then deep-fried, served with fresh lemon wedges and sweet chili sauce.</p></div>
    <div class="item"><div class="item-head">Cajun Shrimp Nuggets<span class="leader"></span><span class="price">10</span></div><p class="desc">Several Gulf shrimp battered in our homemade Cajun seasoning then deep-fried, served with fresh lemon wedges and our remoulade sauce.</p></div>
    <div class="item"><div class="item-head">Southwest Shrimp Skewers<span class="leader"></span><span class="price">10</span></div><p class="desc">6 Gulf shrimp grilled to perfection in garlic and butter, topped with homemade Pico De Gallo and fresh lemon wedges.</p></div>
    <div class="item"><div class="item-head">Chicken Wings<span class="leader"></span><span class="price">10</span></div><p class="desc">Marinated chicken wings deep-fried then hand-tossed into your choice of our homemade buffalo sauce, honey barbeque sauce, honey chipotle or served naked with freshly cut carrots, celery and your choice of sauce.</p></div>
    <div class="item"><div class="item-head">Deep-Fried Pickles<span class="leader"></span><span class="price">8</span></div><p class="desc">A generous portion of pickles tossed in our signature batter then deep-fried, served with a ranch sauce.</p></div>
    <div class="item"><div class="item-head">Mozzarella Sticks<span class="leader"></span><span class="price">8</span></div><p class="desc">Mozzarella cheese seasoned with Italian herbs then deep-fried and served with marinara sauce.</p></div>
    <div class="item"><div class="item-head">Chips &amp; Pico<span class="leader"></span><span class="price">7</span></div><p class="desc">Fresh corn tortilla chips with fresh homemade Pico De Gallo.</p></div>
    <div class="item"><div class="item-head">Fried Green Tomatoes<span class="leader"></span><span class="price">8</span></div><p class="desc">Vine ripe fried green tomatoes with a pimento cheese base and sprinkled with bacon.</p></div>
    <div class="item"><div class="item-head">Loaded Southwest Fries<span class="leader"></span><span class="price">10</span></div><p class="desc">Creole seasoned fries layered with cheddar and parmesan, topped with Pico De Gallo, homemade remoulade and ranch.</p><p class="addon">(Add Chicken for $3* / Add Steak for $5*)<br>*Not included in Trio price</p></div>
    <div class="item"><div class="item-head">Hollis Signature Trio<span class="leader"></span><span class="price">20</span></div><p class="desc">Choose any of the above three full portioned fresh Hors D’oeuvres.</p></div>
  </div>

  <div class="col col-entrees">
    <h2 class="col-title">‘ENTREES</h2>
    <div class="item"><div class="item-head">Tavern BLT 7<span class="leader"></span><span class="price">6</span></div><p class="desc">Tennessee bacon cooked to perfection served with a fresh tomato slice, lettuce and mayo spread on sourdough bread mayonnaise. Served with your choice of side item.</p><p class="addon">(Add Fried Green Tomatoes for $2)</p></div>
    <div class="item"><div class="item-head">Cajun Shrimp Po’boy<span class="leader"></span><span class="price">12</span></div><p class="desc">Cajun breaded Gulf shrimp served on a hoagie bun with fresh tomatoes, lettuce and mayo. Covered with a Cajun remoulade sauce and sprinkled with Creole seasoning. Served with your choice of side item.</p></div>
    <div class="item"><div class="item-head">Buttermilk Battered Chicken Tenders<span class="leader"></span><span class="price">12</span></div><p class="desc">Three huge chicken tenders, breaded and battered then hand-tossed into your choice of our homemade buffalo sauce, honey barbeque sauce, honey chipotle or served regular with your choice of sauce. Served with your choice of side item.</p></div>
    <div class="item"><div class="item-head">Hollis Famous Reuben Sandwich<span class="leader"></span><span class="price">10</span></div><p class="desc">Corned beef, provolone cheese and sauerkraut served on rye bread with signature dressing. Served with your choice of side item.</p></div>
    <div class="item"><div class="item-head">Philly Cheesesteak<span class="leader"></span><span class="price">10</span></div><p class="desc">Mouthwatering Philly cheesesteak grilled with peppers and onions with our signature dressing. Served with your choice of side item.</p></div>
    <div class="item"><div class="item-head">Chicken Sandwich<span class="leader"></span><span class="price">10</span></div><p class="desc">Grilled or fried chicken breast served on a kaiser bun with lettuce, tomato and mayo. Hand-tossed in your choice of our homemade buffalo sauce, honey barbeque sauce, honey chipotle or served naked with freshly cut carrots, celery and your choice of sauce. Served with your choice of side item.</p></div>
    <div class="item"><div class="item-head">Caribbean Grouper Sandwich<span class="leader"></span><span class="price">14</span></div><p class="desc">Caribbean grouper grilled or fried, served on a kaiser roll with lettuce, tomato and mayo. Served with your choice of side item.</p></div>
    <div class="item"><div class="item-head">B&amp;B Steak and Onions*<span class="leader"></span><span class="price">14</span></div><p class="desc">Shoulder top blade steak cooked to your preference. Topped with sauteed onions, crispy bacon bits and bleu cheese crumbles. Served with your choice of side item.</p></div>
    <div class="item"><div class="item-head">Hollis Signature Tavern Burger*<span class="leader"></span><span class="price">10</span></div><p class="desc">Our fresh, never frozen burgers are 100% black angus beef and are made to perfection with your choice of cheddar, Swiss, American or provolone cheese, juicy bacon, your choices of ketchup, mustard or mayo served on a bun with your choice of tomato, lettuce and onion. Served with your choice of side item.</p></div>
    <div class="item"><div class="item-head">Veracruz Quesadilla<span class="leader"></span><span class="price">7</span></div><p class="desc">Wheat tortilla grilled with melted cheese, onions and jalepeno peppers with a side of Pico De Gallo and sour cream. Served with your choice of side item.</p><p class="addon">(Add Chicken for $3 / Add Steak or Shrimp for $5)</p></div>
    <div class="item"><div class="item-head">River City Nachos<span class="leader"></span><span class="price">11</span></div><p class="desc">Fresh corn tortilla chips with fresh homemade Pico De Gallo, melted cheese, onions, jalepeno peppers. Served with your choice of side item.</p><p class="addon">(Add Chicken for $3 / Add Steak or Shrimp for $5)</p></div>
  </div>

  <div class="col col-greens">
    <h2 class="col-title">FRESH GREENS</h2>
    <div class="item"><div class="item-head">House Salad<span class="leader"></span><span class="price">8</span></div><p class="desc">A generous portion of iceberg &amp; romaine lettuce with fresh diced tomatoes, onions and carrots with your choice of ranch, bleu cheese, Italian or balsamic vinaigrette dressing.</p></div>
    <div class="item"><div class="item-head">Caesar Salad<span class="leader"></span><span class="price">8</span></div><p class="desc">A generous portion of romaine lettuce sprinkled with parmesan cheese, croutons with a side of Caesar dressing.</p><p class="addon">Add Grilled or Fried Chicken 3<br>Add Steak* or Shrimp 5</p></div>
    <div class="section-rule"></div>
    <h2 class="col-title">WRAPS</h2>
    <div class="item"><div class="item-head">Veggie Wrap<span class="leader"></span><span class="price">8</span></div><p class="desc">Romaine and iceberg lettuce, onions and tomato wrapped in a wheat tortilla with the dressing of your choice. Served with your choice of side item.</p><p class="addon">Add Grilled or Fried Chicken 3<br>Add Steak* or Shrimp 5</p></div>
    <div class="section-rule"></div>
    <h2 class="col-title">FRESH CATCH</h2>
    <div class="item"><div class="item-head">Garlic Buttered Scallops<span class="leader"></span><span class="price">Market Price</span></div><p class="desc">Three fresh scallops grilled to perfection in butter and served with a side of garlic butter.</p></div>
    <div class="item"><div class="item-head">Fresh Fish of the Day*<span class="leader"></span><span class="price">Market Price</span></div><p class="desc">Ask about the fish of the day, brought in fresh and served to perfection. Seasons vary for amberjack, Chilean seabass, black grouper, mahi, redfish, red snapper, swordfish, tuna or Canadian salmon.</p></div>
    <div class="item"><div class="item-head">Surf and Turf*<span class="leader"></span><span class="price">Market Price</span></div><p class="desc">Fresh catch of the day, grilled in buttered seasoning and served along with an eight ounce shoulder top blade steak covered in onions.</p></div>
  </div>
</section>

</body>
</html>
```